Brightvale Cherries Rainier POS Card 7"H x 11"W

We are wanting to create a one-sided 7 x 11 Rainier cherry card that is eye catching and informative.This should be clear and easy to read and not cluttered. We use these cards as a display in grocery stores, demo stands, and other events to market Brightvale Rainier Cherries. We have a few facts that we would like displayed on the card (see below).

Target Market(s)

Consumers

Industry/Entity Type

Agriculture

Font styles to use
Sans Serif

Requirements
Must have
• Yellow cherries - yellow fruit (the blush on the skin is a kiss from the sun)
• Juice doesn't stain - Kid Friendly
• Add contrast to your summer table
• Sweetest Variety - still low glycemic
• Source of Vitamin C, Source of Potassium, and Source of Melatonin
• Rainiers take up to 4x as much work as red cherries
• Natural Color palettes
• Easy to read
• Brightvale Cherries
Nice to have
• Unique, creative, realistc Rainier cherry designs
Should not have
• pastel or neon color scheme, overly cutesy elements

```html
<!DOCTYPE html>
<html lang="en">
<head>
<meta charset="utf-8">
<title>Brightvale Rainier Cherries – POS Card</title>
<link rel="stylesheet" href="https://fonts.googleapis.com/css2?family=Satisfy&family=Sniglet:wght@800&display=swap">
<style>
  :root {
    --paper: #ffffff;
    --leaf-green: #8aa345;
    --leaf-green-light: #9bb35a;
    --wine: #621e2c;
    --ink-brown: #3a2818;
    --cream: #ffffff;
    --cherry-red: #d8302c;
    --cherry-blush: #f07a55;
    --cherry-gold: #f6c866;
  }
  html, body {
    margin: 0;
    padding: 0;
    overflow: hidden;
    background: var(--paper);
  }
  .card {
    position: relative;
    width: 1200px;
    height: 880px;
    overflow: hidden;
    background: var(--paper);
  }
  .card__field {
    position: absolute;
    left: 0;
    top: 58px;
    width: 1200px;
    height: 762px;
    background: radial-gradient(ellipse at 75% 35%, var(--leaf-green-light), var(--leaf-green) 60%);
  }
  .card__band {
    position: absolute;
    left: 0;
    top: 58px;
    width: 1200px;
    height: 762px;
  }
  .facts,
  .facts__effort {
    position: absolute;
    margin: 0;
    padding: 0;
    font-family: "Sniglet", sans-serif;
    font-weight: 800;
    font-size: 30px;
    line-height: 44px;
    color: var(--ink-brown);
    letter-spacing: 0.3px;
    white-space: nowrap;
  }
  .facts {
    left: 56px;
    top: 96px;
    list-style: none;
  }
  .facts li { margin: 0; }
  .facts__effort {
    left: 66px;
    top: 416px;
  }
  .facts__effort span { display: block; }
  .facts__effort .indent { padding-left: 12px; }
  .cherries-photo {
    position: absolute;
    left: 598px;
    top: 336px;
    width: 542px;
    height: 300px;
    border-radius: 50% 50% 46% 46% / 58% 58% 42% 42%;
    background:
      radial-gradient(circle at 50% 28%, var(--cherry-red), transparent 45%),
      radial-gradient(circle at 25% 72%, var(--cherry-blush), transparent 50%),
      radial-gradient(circle at 80% 75%, var(--cherry-gold), transparent 50%),
      linear-gradient(180deg, #e6503e, #f4a66a);
  }
  .nutrition-ring {
    position: absolute;
    left: 766px;
    top: 130px;
    width: 270px;
    height: 270px;
    border-radius: 50%;
    border: 3px solid rgba(255, 255, 255, 0.45);
    background: rgba(255, 255, 255, 0.1);
    box-sizing: border-box;
  }
  .nutrition {
    position: absolute;
    left: 766px;
    top: 222px;
    width: 316px;
    margin: 0;
    font-family: "Satisfy", cursive;
    font-size: 25px;
    line-height: 34px;
    color: var(--cream);
    text-align: center;
    white-space: nowrap;
  }
  .brand {
    position: absolute;
    left: 30px;
    top: 690px;
    display: flex;
    align-items: center;
    gap: 20px;
    font-family: "Sniglet", sans-serif;
    font-weight: 800;
    font-size: 60px;
    color: var(--cream);
  }
  .brand__dot {
    width: 76px;
    height: 76px;
    border-radius: 50%;
    border: 4px solid var(--cream);
    box-sizing: border-box;
  }
</style>
</head>
<body>
  <main class="card">
    <div class="card__field"></div>
    <svg class="card__band" viewBox="0 0 1200 762" aria-hidden="true">
      <polygon points="0,508 1200,698 1200,762 0,762" fill="var(--wine)"/>
    </svg>

    <ul class="facts">
      <li>- Yellow cherries - yellow fruit</li>
      <li>(the blush on the skin is a kiss from the sun</li>
      <li>- Add contrast to</li>
      <li>your summer table</li>
      <li>- Juice doesn’t stain- Kid Friendly</li>
      <li>- Sweetest Variety</li>
      <li>- still low glycemic</li>
    </ul>

    <p class="facts__effort">
      <span>-Rainiers take up to 4x</span>
      <span>as much work as</span>
      <span class="indent">red cherries!</span>
    </p>

    <div class="cherries-photo" role="img" aria-label="Photo of a heap of yellow and red-blushed Rainier cherries with stems, one cut in half showing the pit"></div>
    <div class="nutrition-ring"></div>
    <p class="nutrition">Source of Vitamin C,<br>Source of Potassium,<br>and Source of Melatonin</p>

    <div class="brand">
      <span class="brand__dot"></span>
      <span class="brand__name">Brightvale Cherries</span>
    </div>
  </main>
</body>
</html>
```